International business needs business cards

Our company, DOR Ventures Inc. is in the business of supplying a range construction products with particular emphasis on CEMENT. We have developed our own brand - BRUNVALE MATERIALS - with which to infiltrate the market. We are launching our brand of cement (BRUNVALE Type IS Cement) into the Caribbean which is unlike anything this market has ever seen. A monopoly has existed here for the past 60-odd years and the market has now opened to allow the importation of other brands and consumers are anxious and ready for change/improvement. We are very excited to be launching and want to make a great first impression. We will be conducting workshops and seminars (from government level to the hardware store owners) and we want our business card to give us the strong, confident introduction that we need.

Target Market(s)

construction; builders; engineers; home owners

Industry/Entity Type

Construction

Contact Information for Business Card

Marisol Penwick
CEO
cell # 1 555 4817730
Ground floor,Lantern Plaza Suite 2483
George Town,Grand Cayman
Cayman Islands,KY1-2250
EMAIL: m.penwick@dorventuresinc.example
web site dorventuresinc.example

COMPANY: skype info dor.ventures.example

second card
Tamsin Rowe-Penwick
CFO
CELL# 1 555 604 3917
George Town,Grand Cayman
Cayman Islands,KY1-2250
EMAIL: t.rowepenwick@dorventuresinc.example
website dorventuresinc.example

Requirements
Must have
• Business cards must display BOTH logos - DOR is the company and BRUNVALE is the brand.

```html
<!DOCTYPE html>
<html lang="en">
<head>
<meta charset="utf-8">
<title>DOR Ventures Inc. – Business Card</title>
<link rel="stylesheet" href="https://fonts.googleapis.com/css2?family=Source+Sans+3:wght@400;600;700&display=swap">
<style>
  :root {
    --stage-top: #2b2b2b;
    --stage-bottom: #040404;
    --card-light: #f3f3f3;
    --brand-maroon: #7d1418;
    --ink: #1a1a1a;
    --ink-soft: #3a3a3a;
    --white: #ffffff;
  }
  * { margin: 0; padding: 0; box-sizing: border-box; }
  html, body { width: 1200px; height: 900px; overflow: hidden; }
  body {
    background: linear-gradient(180deg, var(--stage-top) 0%, #161616 55%, var(--stage-bottom) 100%);
    font-family: "Source Sans 3", "Myriad Pro", sans-serif;
    position: relative;
  }
  .card {
    position: absolute;
    top: 184px;
    width: 302px;
    height: 491px;
    border-radius: 12px;
    overflow: hidden;
  }
  .card--front { left: 299px; background: var(--card-light); }
  .card--back { left: 646px; background: var(--brand-maroon); }

  .company-mark {
    position: absolute;
    display: flex;
    align-items: center;
    gap: 10px;
    font-weight: 700;
    white-space: nowrap;
  }
  .company-mark__square { width: 40px; height: 40px; flex: none; }
  .company-mark__name { font-size: 23px; line-height: 1; letter-spacing: 0.2px; }

  .card--front .company-mark { left: 0; right: 0; top: 52px; justify-content: center; }
  .card--front .company-mark__square { background: var(--brand-maroon); }
  .card--front .company-mark__name { color: var(--ink); }

  .card--back .company-mark { left: 0; right: 0; top: 394px; justify-content: center; }
  .card--back .company-mark__square { background: var(--white); }
  .card--back .company-mark__name { color: var(--white); }

  .person { position: absolute; top: 173px; left: 0; right: 0; text-align: center; }
  .person__name { color: var(--brand-maroon); font-weight: 600; font-size: 18.5px; line-height: 1.2; }
  .person__role { color: var(--ink); font-size: 13.5px; line-height: 1.3; }

  .address {
    position: absolute; top: 239px; left: 0; right: 0;
    text-align: center; font-style: normal;
    color: var(--ink); font-size: 13.5px; line-height: 20px;
  }
  .contacts {
    position: absolute; top: 325px; left: 0; right: 0;
    list-style: none; text-align: center;
    color: var(--ink); font-size: 13.5px; line-height: 20px;
  }
  .contacts li { display: flex; justify-content: center; align-items: center; gap: 3px; }
  .contacts svg { width: 10px; height: 10px; fill: var(--brand-maroon); flex: none; }

  .brand-mark {
    position: absolute; top: 428px; left: 0; right: 0;
    text-align: center;
    color: var(--ink-soft); font-weight: 700; font-size: 12px; letter-spacing: 1.5px;
  }
</style>
</head>
<body>
  <section class="card card--front" aria-label="Business card front">
    <div class="company-mark">
      <span class="company-mark__square"></span>
      <span class="company-mark__name">DOR Ventures Inc.</span>
    </div>

    <div class="person">
      <p class="person__name">Marisol Penwick</p>
      <p class="person__role">CEO</p>
    </div>

    <address class="address">
      Ground floor, Lantern Plaza Suite 2483<br>
      George Town, Grand Cayman<br>
      Cayman Islands, KY1-2250
    </address>

    <ul class="contacts">
      <li>
        <svg viewBox="0 0 10 10" aria-hidden="true"><path d="M2 0.5 L3.6 0.5 L4.3 2.8 L3.2 3.7 C3.8 5 4.9 6.2 6.3 6.8 L7.2 5.7 L9.5 6.4 L9.5 8 C9.5 9 8.7 9.6 7.8 9.5 C4 9 1 6 0.5 2.2 C0.4 1.3 1 0.5 2 0.5 Z"/></svg>
        1 555 4817730
      </li>
      <li>
        <svg viewBox="0 0 10 10" aria-hidden="true"><path d="M0 2 H10 V8.5 H0 Z M0.6 2.4 L5 5.6 L9.4 2.4" stroke="#f3f3f3" stroke-width="0.8"/></svg>
        m.penwick@dorventuresinc.example
      </li>
      <li>
        <svg viewBox="0 0 10 10" aria-hidden="true"><circle cx="5" cy="5" r="4.8"/><path d="M2.5 3 C4 2.5 4.5 4 3.5 5 C3 6 4.5 7 4 8.5 M6.5 2 C6 3.5 7.5 4 8.5 4.5 M6 6.5 C6.5 7.5 7.5 7.5 8 6.8" stroke="#f3f3f3" stroke-width="0.7" fill="none"/></svg>
        www.dorventuresinc.example
      </li>
    </ul>

    <p class="brand-mark">BRUNVALE</p>
  </section>

  <section class="card card--back" aria-label="Business card back">
    <div class="company-mark">
      <span class="company-mark__square"></span>
      <span class="company-mark__name">DOR Ventures Inc.</span>
    </div>
  </section>
</body>
</html>
```